A Visual Masterpiece for an Optometry Practice

We are looking for a web designer to create a website for our optometry business that makes the client appreciate the gift of sight. We are looking for something clean and crisp but beautiful and compelling. Something that is unique and experiencial. So if you are up for the artistic challenge, lets journey together and create something amazing. We look forward to working with you!
Updates

I updated the source files for the logos. Thanks for letting me know that the other ones did not work. Thanks everyone!

I am extending the deadline due to the fact that there has only been a few submissions. This does not reflect the quality of the subissions, but we are looking for a larger pool to choose from. Thank you so much for your flexibility and patience. We appreciate you and the work you have done =)

Target Market(s)

This business is in Lancaster, Ohio which is mainly hosts mainly blue-colared families. We believe that a lot of times people do not come to an optometrist until something is wrong with their eyes, and we would love to change that. We want to bring awareness to how amazing the gift of sight is and want to focus on beauty, adventure and playfulness. With this being said, we want our website to be full of wonder, beauty and adventure. something that makes someone say, "check this out! This is freaking amazing!"

Industry/Entity Type

Business

Requirements
Must have
• Home Page
Location Page
Contact Page
"Register Online" Page
Philophy Page
Stories page (simular to a testimonial)

We would like it to be very user friendly and able to be updated easily by one of our nurses

also, I have uploaed source files of our logo for you to insert on each page.

If you have ideas or concepts that would include actual photos of the doctor or day to day activities, we can hire a photographer for quality images. We didnt want to do that prior to picking the designer.
Nice to have
• We would love it to feel simple but at the same time full of life. Wed love for the site to take the eye on a journey.

```html
<!DOCTYPE html>
<html lang="en">
<head>
<meta charset="utf-8">
<title>Brightfield Optometry</title>
<link rel="stylesheet" href="https://fonts.googleapis.com/css2?family=Arimo:wght@400;700&family=Open+Sans:wght@300;400;600&display=swap">
<style>
:root{
  --green:#0c4f3c;
  --green-dark:#083d2e;
  --coral:#f58a6a;
  --coral-ring:#ee8a6e;
  --ink:#222;
  --body:#555;
  --muted:#888;
  --line:#c9c9c9;
  --tab-top:#f4f4f4;
  --tab-bottom:#d2d2d2;
  --frame:#9a9a9a;
}
*{box-sizing:border-box;margin:0;padding:0}
html,body{width:865px;height:1200px;overflow:hidden;background:#fff}
body{position:relative;font-family:Arimo,Arial,sans-serif;color:var(--ink)}
.abs{position:absolute}
.page{left:43px;top:37px;width:789px;height:1090px;border-radius:12px;background:linear-gradient(#f3f3f3 0,#fff 140px);box-shadow:0 2px 6px rgba(0,0,0,.35)}
.eye-badge{left:29px;top:6px;width:70px;height:70px;border-radius:50%;background:linear-gradient(160deg,#fbfbfb,#e4e1de 60%,#d8d2cc);box-shadow:0 1px 4px rgba(0,0,0,.3)}
.brand{left:60px;top:88px;display:flex;align-items:center;gap:12px;font-family:"Open Sans",sans-serif;font-weight:300;color:var(--green)}
.brand-mark{width:56px;height:56px;background:#e9a06a;opacity:.85}
.brand-name{font-size:34px;line-height:36px}
.brand-sub{font-size:13px;letter-spacing:9px;display:block;line-height:18px}
.account{left:727px;top:54px;font-size:11px;color:#111}
.account span{margin:0 8px}
.search{left:629px;top:91px;width:181px;height:27px;border:1px solid #bbb;border-radius:5px;background:#fff;box-shadow:inset 0 1px 2px rgba(0,0,0,.15)}
.search-label{left:17px;top:6px;font-size:11px;color:#999}
.search-go{right:3px;top:2px;width:31px;height:21px;border-radius:4px;background:var(--green);color:#fff;font-size:11px;text-align:center;line-height:21px}
.nav{top:145px;height:29px;border:1px solid #aaa;border-bottom:none;border-radius:4px 4px 0 0;background:linear-gradient(var(--tab-top),var(--tab-bottom));font-size:12px;text-align:center;line-height:29px;color:#111;white-space:nowrap}
.nav.is-active{background:linear-gradient(#1a6a52,var(--green-dark));color:#fff;border-color:var(--green-dark)}
.hero{left:48px;top:178px;width:782px;height:277px;background:var(--frame)}
.hero-main{left:53px;top:182px;width:553px;height:267px;background:linear-gradient(#d9d9d9,#f0f0f0 45%,#8d8d8d)}
.hero-caption{left:55px;top:418px;width:549px;height:29px;background:rgba(30,30,30,.75);color:#fff;font-size:11.5px;letter-spacing:-.15px;line-height:29px;padding-left:33px;white-space:nowrap}
.hero-arrow{top:303px;width:22px;height:30px;background:#fff;font-size:16px;line-height:30px;text-align:center;color:#333;font-weight:700}
.thumb{left:621px;width:199px;background:linear-gradient(#c9a77f,#8d7660)}
.thumb-label{left:0;width:100%;text-align:center;color:#fff;font-size:12px;font-weight:700;text-shadow:0 0 3px #000,0 0 2px #000}
.panel{left:54px;width:206px;border:1px solid #ccc;background:linear-gradient(#fff,#f0f0f0);box-shadow:0 3px 5px rgba(0,0,0,.12)}
.panel-title{height:28px;background:var(--green);color:#fff;font-size:13px;line-height:28px;letter-spacing:.3px;box-shadow:0 2px 3px rgba(0,0,0,.3)}
.field{left:71px;width:175px;border:1px solid #bbb;border-radius:5px;background:#fff;font-size:11px;color:#999;padding:7px 0 0 20px;letter-spacing:.4px;box-shadow:inset 0 1px 2px rgba(0,0,0,.1)}
.field.is-tall{padding-top:16px}
.btn-submit{height:28px;background:var(--green);color:#fff;border-radius:4px;font-size:12px;line-height:28px;text-align:center}
.map{left:70px;top:962px;width:174px;height:125px;border:1px solid #bbb;background:linear-gradient(135deg,#e3e3dc,#cfd0c9)}
.section-tab{left:277px;width:271px;height:32px;background:linear-gradient(90deg,#e6e6e6,#f7f7f7);box-shadow:0 2px 3px rgba(0,0,0,.1);font-family:"Open Sans",sans-serif;font-size:15px;line-height:32px;padding-left:22px;letter-spacing:1px;color:#444;white-space:nowrap}
.section-tab b{color:var(--green);font-weight:600}
.photo{border:3px solid var(--coral-ring);border-radius:50%;background:linear-gradient(#eadfd6,#b9a596);box-shadow:0 2px 4px rgba(0,0,0,.3)}
.welcome-text{left:440px;top:518px;width:380px;font-family:"Open Sans",sans-serif;font-size:9.6px;letter-spacing:-.05px;line-height:15px;color:var(--body)}
.welcome-text p+p{margin-top:15px}
.btn-more{width:64px;height:22px;background:var(--coral);color:#333;font-size:8px;line-height:22px;text-align:center;box-shadow:0 1px 2px rgba(0,0,0,.2);letter-spacing:-.2px;white-space:nowrap}
.divider{left:303px;width:525px;border-top:1px dotted #7fb7b0}
.story-name{font-family:"Open Sans",sans-serif;font-size:11px;letter-spacing:1px;color:#555}
.story-meta,.story-text{font-size:9px;line-height:11px;color:#333;width:150px}
.footer-links{left:333px;top:1154px;font-size:10px;color:#111;white-space:nowrap}
.footer-links span{margin:0 11px}
.copyright{left:407px;top:1180px;font-size:10px;color:#111;white-space:nowrap}
.social{top:1160px;width:23px;height:23px;border-radius:50%;background:linear-gradient(#4c8fd0,#205d9e)}
</style>
</head>
<body>
<div class="abs page"></div>
<div class="abs eye-badge" role="img" aria-label="Close-up photograph of a human eye"></div>

<header>
  <div class="abs brand">
    <div class="brand-mark"></div>
    <div class="brand-name">Brightfield<span class="brand-sub">OPTOMETRY</span></div>
  </div>
  <div class="abs account">Log In<span>|</span>Register</div>
  <div class="abs search"><span class="abs search-label">Search</span><span class="abs search-go">Go</span></div>
  <nav>
    <div class="abs nav is-active" style="left:330px;width:97px">HOME</div>
    <div class="abs nav" style="left:431px;width:97px">ABOUT US</div>
    <div class="abs nav" style="left:532px;width:97px">SERVICES</div>
    <div class="abs nav" style="left:633px;width:96px">FIND&nbsp; DOCTOR</div>
    <div class="abs nav" style="left:733px;width:98px">CONTACT US</div>
  </nav>
</header>

<section>
  <div class="abs hero"></div>
  <div class="abs hero-main" role="img" aria-label="Bright modern eyewear showroom interior"></div>
  <div class="abs hero-caption">Lorem ipsum dolor sit amet, consectetuer&nbsp; adipiscing elit.Lorem ipsum dolor sit amet, adipiscing&nbsp; elit</div>
  <div class="abs hero-arrow" style="left:44px;border-radius:0 15px 15px 0">»</div>
  <div class="abs hero-arrow" style="left:593px;border-radius:15px 0 0 15px">«</div>
  <div class="abs thumb" style="top:182px;height:131px" role="img" aria-label="Woman browsing a wall of designer frames">
    <div class="abs thumb-label" style="top:106px">DESIGNER FRAMES:</div>
  </div>
  <div class="abs thumb" style="top:321px;height:126px;background:linear-gradient(#f0f0f0,#c9b3a2)" role="img" aria-label="Man holding up a pair of sunglasses">
    <div class="abs thumb-label" style="top:104px">SUNGLASSES</div>
  </div>
</section>

<aside>
  <div class="abs panel" style="top:474px;height:251px"></div>
  <div class="abs panel-title" style="left:62px;top:481px;width:187px;padding-left:23px">ONLINE APPOINTMENT</div>
  <div class="abs field" style="top:526px;height:27px">Your name</div>
  <div class="abs field" style="top:560px;height:27px">Email</div>
  <div class="abs field" style="top:594px;height:27px">Phone</div>
  <div class="abs field is-tall" style="top:628px;height:52px">Message</div>
  <div class="abs btn-submit" style="left:72px;top:689px;width:68px">SUBMIT</div>

  <div class="abs panel" style="top:750px;height:351px"></div>
  <div class="abs panel-title" style="left:62px;top:759px;width:192px;padding-left:28px">CONTACT&nbsp; FORM</div>
  <div class="abs field" style="top:798px;height:27px">Name</div>
  <div class="abs field" style="top:832px;height:27px">Email</div>
  <div class="abs field is-tall" style="top:869px;height:40px;padding-top:13px">Message</div>
  <div class="abs btn-submit" style="left:75px;top:921px;width:68px">SUBMIT</div>
  <div class="abs map" role="img" aria-label="Street map showing the practice location"></div>
  <svg class="abs" style="left:131px;top:1002px" width="12" height="18" viewBox="0 0 12 18" aria-hidden="true"><path d="M6 0a6 6 0 0 1 6 6c0 4-6 12-6 12S0 10 0 6a6 6 0 0 1 6-6z" fill="#c8302a"/><circle cx="6" cy="6" r="2" fill="#7a1a16"/></svg>
</aside>

<main>
  <div class="abs section-tab" style="top:469px">WELCOME TO <b>BRIGHTFIELD</b></div>
  <div class="abs photo" style="left:286px;top:513px;width:128px;height:130px" role="img" aria-label="Optometrist fitting glasses for a patient"></div>
  <div class="abs welcome-text">
    <p>Lorem Ipsum is simply dummy text of the printing and typesetting industry. Lorem Ipsum has been the industry's standard dummy text ever since the 1500s, when an unknown printer took a galley of type and scrambled it to make a type specimen book.</p>
    <p>It has survived not only five centuries, but also the leap into electronic typesetting, remaining essentially unchanged. It was popularised in the 1960s with the release of Letraset</p>
  </div>
  <div class="abs btn-more" style="left:751px;top:644px">READ MORE</div>
  <div class="abs divider" style="top:686px"></div>

  <div class="abs section-tab" style="top:694px">SUCCESS&nbsp; <b>STORIES</b></div>

  <div class="abs photo" style="left:295px;top:738px;width:77px;height:108px" role="img" aria-label="Portrait of a smiling patient"></div>
  <div class="abs story-name" style="left:382px;top:737px">DALE</div>
  <div class="abs story-meta" style="left:383px;top:763px">25 years old, Diagnosis:<br>Diabetic Retinopathy and Auto Accident</div>
  <div class="abs story-text" style="left:383px;top:808px">Dale was involved in an automobile accident while on the job, sustaining an injury to his one functional eye.</div>
  <div class="abs btn-more" style="left:385px;top:851px">READ MORE</div>

  <div class="abs photo" style="left:581px;top:733px;width:77px;height:108px" role="img" aria-label="Portrait of a smiling patient wearing glasses"></div>
  <div class="abs story-name" style="left:672px;top:732px">MARIAN</div>
  <div class="abs story-meta" style="left:672px;top:756px">60 years old, Diagnosis: Macular</div>
  <div class="abs story-text" style="left:672px;top:778px">Marian was experiencing difficulty reading, working crossword puzzles, and playing cards due to her vision loss. When completing cooking tasks.</div>
  <div class="abs btn-more" style="left:675px;top:847px">READ MORE</div>

  <div class="abs divider" style="top:903px"></div>

  <div class="abs photo" style="left:295px;top:937px;width:77px;height:109px" role="img" aria-label="Patient during an eye examination"></div>
  <div class="abs story-name" style="left:382px;top:935px">DALE</div>
  <div class="abs story-meta" style="left:383px;top:960px">25 years old, Diagnosis:<br>Diabetic Retinopathy and Auto Accident</div>
  <div class="abs story-text" style="left:383px;top:1004px">Dale was involved in an automobile accident while on the job, sustaining an injury to his one functional eye.</div>
  <div class="abs btn-more" style="left:382px;top:1049px">READ MORE</div>

  <div class="abs photo" style="left:585px;top:936px;width:77px;height:110px" role="img" aria-label="Portrait of a patient wearing glasses"></div>
  <div class="abs story-name" style="left:672px;top:930px">MARIAN</div>
  <div class="abs story-meta" style="left:672px;top:954px">25 years old, Diagnosis: Macular</div>
  <div class="abs story-text" style="left:672px;top:976px">Marian was experiencing difficulty reading, working crossword puzzles, and playing cards due to her vision loss. When completing cooking tasks.</div>
  <div class="abs btn-more" style="left:672px;top:1048px">READ MORE</div>
</main>

<footer>
  <div class="abs social" style="left:63px" aria-label="Social profile"></div>
  <div class="abs social" style="left:95px;background:linear-gradient(#8ad3f0,#3aa4d4)" aria-label="Social profile"></div>
  <div class="abs social" style="left:128px;background:linear-gradient(#4f9fd6,#1d6aa6)" aria-label="Social profile"></div>
  <div class="abs social" style="left:160px;background:linear-gradient(#f9b160,#e2741e)" aria-label="News feed"></div>
  <div class="abs footer-links">PRIVACY POLICY<span>|</span>DISCLAIMER<span>|</span>TERMS &amp; CONDITIONS<span>|</span>CONTACT US</div>
  <div class="abs copyright">Copyright © Brightfield, All Rights Reserved</div>
</footer>
</body>
</html>
```